I have a tallow based business and I want to streamline my products

I have roughly 10 items that I would like to make lebals for in order to streamline my business, I am attaching the current design and am willing to work with this but would also like to see if you come up with something different, my biggest seller is my facewash , my webpage is themeadowlyco,com my current designs are below- The newest one is the light brown version which I do like but I am not sure how that will integrate or be streamlined with the remaining products, If you believe it can look similar and still be attractive, I am ok with that too,

My current Label Project Needs:

Tallow + Magnesium Lotion biodegradable wheat bottle
Tallow Cream Face Wash - biodegradable what bottle
Tallow Body Butter 8 oz jar with bamboo lid
Tallow Deodorant will be printed on a Kraft Paper tube
Tallow Face Cream for Day wear 2 oz glass jar with bamboo lid
Vitamin C Serum 2 oz serum bottle with bamboo pump
Blue Algae Toner 4 oz glass bottle
Tallow + Hyaluronic 2oz face cream jar
'
My project is to display sustainable products, eco friendly packaging, organic , natural and holistic

I am ok with the newest label I attached but I am also ok with a minimalistic project, I would love to choose from a couple of designs.

Thank you so much

```html
<!DOCTYPE html>
<html lang="en">
<head>
<meta charset="utf-8">
<title>The Meadowly Co. – Tallow Cream Face Wash Label</title>
<link href="https://fonts.googleapis.com/css2?family=Oswald:wght@500;600;700&family=Anton&family=Great+Vibes&display=swap" rel="stylesheet">
<style>
  :root {
    --label-cream: #f8f6ee;
    --ink-teal: #1a6e8b;
    --sun-orange: #f0a323;
    --sun-deep: #e48f12;
  }
  html, body {
    margin: 0;
    padding: 0;
    width: 1000px;
    height: 1200px;
    overflow: hidden;
    background: var(--label-cream);
  }
  .label {
    position: relative;
    width: 1000px;
    height: 1200px;
    color: var(--ink-teal);
    font-family: "Oswald", "Arial Narrow", sans-serif;
  }
  .brand-arc {
    position: absolute;
    left: 200px;
    top: 60px;
    width: 600px;
    height: 200px;
  }
  .brand-arc text {
    font-family: "Oswald", "Arial Narrow", sans-serif;
    font-weight: 600;
    font-size: 54px;
    letter-spacing: 2px;
    fill: var(--ink-teal);
  }
  .hero-art {
    position: absolute;
    left: 250px;
    top: 210px;
    width: 500px;
    height: 340px;
    border-radius: 250px 250px 0 0;
    background: radial-gradient(circle at 55% 60%, var(--sun-orange) 0%, var(--sun-deep) 55%, var(--ink-teal) 130%);
  }
  .product-title {
    position: absolute;
    left: 0;
    width: 1000px;
    text-align: center;
    font-family: "Anton", "Oswald", sans-serif;
    font-size: 170px;
    line-height: 1;
    letter-spacing: 2px;
    color: var(--ink-teal);
    margin: 0;
  }
  .product-title.first { top: 565px; }
  .product-title.second { top: 770px; }
  .product-variant {
    position: absolute;
    left: 0;
    width: 1000px;
    top: 700px;
    text-align: center;
    font-family: "Great Vibes", cursive;
    font-size: 110px;
    line-height: 1;
    color: var(--sun-orange);
  }
  .divider {
    position: absolute;
    left: 210px;
    top: 975px;
    width: 580px;
    height: 30px;
  }
  .benefits {
    position: absolute;
    left: 0;
    width: 1000px;
    top: 1020px;
    text-align: center;
    font-weight: 600;
    font-size: 44px;
    letter-spacing: 1px;
    margin: 0;
  }
  .net-weight {
    position: absolute;
    left: 0;
    width: 1000px;
    top: 1100px;
    text-align: center;
    font-weight: 500;
    font-size: 28px;
    letter-spacing: 1px;
    margin: 0;
  }
</style>
</head>
<body>
  <main class="label">
    <svg class="brand-arc" viewBox="0 0 600 200" aria-label="The Meadowly Co.">
      <defs>
        <path id="brand-curve" d="M 40 190 Q 300 20 560 190" fill="none"/>
      </defs>
      <text text-anchor="middle"><textPath href="#brand-curve" startOffset="50%">THE MEADOWLY CO.</textPath></text>
    </svg>

    <div class="hero-art" role="img" aria-label="Illustration of a spotted cow standing in front of a rising sun"></div>

    <h1 class="product-title first">FACE</h1>
    <div class="product-variant">Tallow Cream</div>
    <h1 class="product-title second">WASH</h1>

    <svg class="divider" viewBox="0 0 580 30" aria-hidden="true">
      <line x1="0" y1="15" x2="255" y2="12" stroke="var(--ink-teal)" stroke-width="4" stroke-linecap="round"/>
      <circle cx="290" cy="15" r="9" fill="var(--ink-teal)"/>
      <line x1="325" y1="12" x2="580" y2="15" stroke="var(--ink-teal)" stroke-width="4" stroke-linecap="round"/>
    </svg>

    <p class="benefits">CLEANSE • PURIFY • MOISTURIZE</p>
    <p class="net-weight">NET WT. 236ML</p>
  </main>
</body>
</html>
```